Flyer Design Project

We are a storm restoration company that has recently begun restoration from water/flood damage from Hurricane Sandy. We provide disaster relief to homeowners and or commercial property owners after a flood. To start we offer cleanup and remediation which is taking out and disposing of all wet items in a home or business and the cutting out of walls, flooring and other items affected by a flood. We then provide remediation which includes the drying out of a home or business along with a dehumidifier to take all the moisture out of the air and to put it simply dry out the home. We also uses chemicals to clean and provide mold remediation to prevent to growth of mold. We work directly with a customers insurance company if they have flood insurance and after that we provide the services to rebuild and bring their property back to its condition before the storm.

Im looking for an informational type flier that I could insert into our business folders that we give to customers and also to use as fliers to pass out to potential customers. I want potential customers to look at this and feel comfortable with calling my company and working with us.

Company name Bellridge Building Partners. I attached our company logo.

Target Market(s)

Those affected by flooding from Hurricane Sandy

Industry/Entity Type

Insurance

Requirements
Must have
• Company logo, name and colors on flier
Nice to have
• Color photos that have to do with water restoration or showing flood damamge

```html
<!DOCTYPE html>
<html lang="en">
<head>
<meta charset="utf-8">
<title>Bellridge Building Partners – Flood Restoration Flyer</title>
<link href="https://fonts.googleapis.com/css2?family=Open+Sans:wght@400;700;800&display=swap" rel="stylesheet">
<style>
  :root{
    --page-bg:#ffffff;
    --paper:#ffffff;
    --navy:#1f2d5c;
    --headline-blue:#3a8fd6;
    --star-red:#e8452c;
    --band-orange:#e4572e;
    --diagonal-grey:#d4d5d7;
  }
  html,body{margin:0;padding:0;}
  body{
    width:1169px;height:1200px;overflow:hidden;
    background:var(--page-bg);
    font-family:"Open Sans",Arial,sans-serif;
  }
  .flyer{
    position:absolute;left:225px;top:0;
    width:563px;height:940px;
    background:var(--paper);
    transform:scale(1.2766);transform-origin:0 0;
    overflow:hidden;
  }
  .flyer__backdrop{position:absolute;left:0;top:0;}
  .brand{
    position:absolute;left:34px;top:70px;
    display:flex;align-items:center;gap:10px;
  }
  .brand__mark{width:26px;height:26px;background:var(--navy);}
  .brand__name{
    margin:0;color:var(--navy);font-weight:800;
    font-size:21px;line-height:24px;letter-spacing:-0.3px;
  }
  .headline{
    position:absolute;left:32px;top:208px;margin:0;
    color:var(--headline-blue);font-weight:800;
    letter-spacing:-2px;line-height:1;
  }
  .headline__small{display:block;font-size:47px;}
  .headline__large{display:block;font-size:84px;letter-spacing:-4px;margin-top:-2px;}
  .services{
    position:absolute;left:24px;top:346px;width:455px;
    margin:0;padding:0;list-style:none;
  }
  .services__item{
    position:relative;padding-left:28px;margin-bottom:22px;
    color:var(--navy);font-size:15.6px;line-height:22.8px;
    text-align:justify;
  }
  .services__star{position:absolute;left:0;top:3px;width:18px;height:18px;}
  .photo-strip{position:absolute;left:0;top:748px;width:563px;height:172px;display:flex;}
  .photo-strip__flooded-house{width:265px;height:100%;background:linear-gradient(180deg,#8a9a63 0%,#6b7451 55%,#5a5a45 100%);}
  .photo-strip__damaged-room{flex:1;height:100%;margin-left:2px;background:linear-gradient(180deg,#bdb8ad 0%,#8c8478 60%,#5c554c 100%);}
  .footer-band{position:absolute;left:0;top:920px;width:563px;height:20px;background:var(--band-orange);}
</style>
</head>
<body>
<main class="flyer">
  <svg class="flyer__backdrop" width="563" height="940" viewBox="0 0 563 940">
    <defs>
      <linearGradient id="hallway-tones" x1="0" y1="0" x2="0" y2="1">
        <stop offset="0" stop-color="#c9ccc9"/>
        <stop offset="0.45" stop-color="#8f8a78"/>
        <stop offset="1" stop-color="#2f3427"/>
      </linearGradient>
    </defs>
    <polygon points="138,0 563,0 563,615" fill="var(--diagonal-grey)"/>
    <polygon points="172,0 563,0 563,405" fill="url(#hallway-tones)" role="img" aria-label="Photo of a flooded office hallway with water covering the floor"/>
  </svg>

  <div class="brand">
    <span class="brand__mark"></span>
    <p class="brand__name">Bellridge Building<br>Partners</p>
  </div>

  <h1 class="headline">
    <span class="headline__small">LET US</span>
    <span class="headline__large">HELP YOU</span>
  </h1>

  <ul class="services">
    <li class="services__item">
      <svg class="services__star" viewBox="0 0 24 24"><polygon points="12,1 15,9 23.5,9 16.7,14.2 19.2,22.5 12,17.4 4.8,22.5 7.3,14.2 0.5,9 9,9" fill="var(--star-red)"/></svg>
      We offer cleanup and remediation which is taking out and disposing of all wet items in a home or business and the cutting out of walls, flooring and other items affected by a flood.
    </li>
    <li class="services__item">
      <svg class="services__star" viewBox="0 0 24 24"><polygon points="12,1 15,9 23.5,9 16.7,14.2 19.2,22.5 12,17.4 4.8,22.5 7.3,14.2 0.5,9 9,9" fill="var(--star-red)"/></svg>
      We then provide remediation which includes the drying out of a home or business along with a dehumidifier to take all the moisture out of the air and to put it simply dry out the home.
    </li>
    <li class="services__item">
      <svg class="services__star" viewBox="0 0 24 24"><polygon points="12,1 15,9 23.5,9 16.7,14.2 19.2,22.5 12,17.4 4.8,22.5 7.3,14.2 0.5,9 9,9" fill="var(--star-red)"/></svg>
      We also uses chemicals to clean and provide mold remediation to prevent to growth of mold.
    </li>
    <li class="services__item">
      <svg class="services__star" viewBox="0 0 24 24"><polygon points="12,1 15,9 23.5,9 16.7,14.2 19.2,22.5 12,17.4 4.8,22.5 7.3,14.2 0.5,9 9,9" fill="var(--star-red)"/></svg>
      We work directly with a customers insurance company if they have flood insurance and after that we provide the services to rebuild and bring their property back to its condition before the storm.
    </li>
  </ul>

  <div class="photo-strip">
    <div class="photo-strip__flooded-house" role="img" aria-label="Photo of a house surrounded by floodwater and trees"></div>
    <div class="photo-strip__damaged-room" role="img" aria-label="Photo of a flood-damaged living room with debris and a fireplace"></div>
  </div>
  <div class="footer-band"></div>
</main>
</body>
</html>
```